Adelaide based cleaning and remediation business needs a website design

We are launching a new company with no clients as yet so we don't have the benefit of Veltrano Ratings to build confidence. We can use our  past work history with other employers in the industry to give some credibility. Happy to use any colour scheme as long as it look interesting when people click on the site it gets there attention. enquiry . I have supplied a mock up the important information and various photos as they tell a lot of the story.

```html
<!DOCTYPE html>
<html lang="en">
<head>
<meta charset="utf-8">
<title>Kestrel Services Pty Ltd</title>
<link href="https://fonts.googleapis.com/css2?family=Poppins:wght@400;500;600;700;800&display=swap" rel="stylesheet">
<style>
:root{--orange:#f47320;--dark:#24282b;--ink:#1e1e1e;--text:#444;--white:#fff;--light:#f4f4f4}
*{box-sizing:border-box;margin:0;padding:0}
html,body{width:1200px;height:3631px;overflow:hidden}
body{font-family:'Poppins',sans-serif;color:var(--ink);background:var(--white);position:relative}
.abs{position:absolute}
.btn{position:absolute;display:flex;align-items:center;justify-content:center;font-weight:700;font-size:13px;text-transform:uppercase;letter-spacing:.2px}
.btn-orange{background:var(--orange);color:var(--white)}
.btn-white{background:var(--white);color:var(--ink)}
/* header */
.logo-frame{left:103px;top:8px;width:155px;height:173px;border-left:6px solid var(--orange);border-bottom:6px solid var(--orange);background:var(--white);z-index:3;display:flex;align-items:center;justify-content:center}
.logo-frame span,.foot-logo span{font-weight:700;font-size:20px;color:var(--ink);letter-spacing:1px}
.topphone{left:700px;top:24px;display:flex;align-items:center;gap:14px;font-weight:600;font-size:17px}
.nav{left:363px;top:94px;display:flex;gap:31px;font-size:13.5px;font-weight:600;text-transform:uppercase}
.nav .active{color:var(--orange);border-bottom:2px solid var(--orange);padding-bottom:4px}
.soc{width:38px;height:38px;border:1.5px solid #555;border-radius:50%;position:absolute}
/* hero */
.hero{left:0;top:137px;width:1200px;height:643px;background:linear-gradient(100deg,#1b1d18 0%,#2f2f28 35%,#6b6d6a 60%,#4a4c48 100%)}
.hero h1{position:absolute;left:111px;top:310px;font-size:62px;font-weight:800;color:var(--white);line-height:1}
.hero h2{position:absolute;left:111px;top:380px;font-size:38px;font-weight:400;color:var(--white);line-height:1}
.hero p{position:absolute;left:111px;top:432px;width:380px;font-size:19px;line-height:28.5px;color:var(--white);font-weight:500}
.callbox{left:687px;top:630px;width:418px;height:94px;background:var(--orange);color:var(--white);display:flex;align-items:center;padding-left:65px;gap:18px}
.callbox small{font-size:12px;display:block}
.callbox b{font-size:23px;font-weight:700}
/* about */
.about-accent{left:687px;top:1100px;width:418px;height:155px;background:var(--orange)}
.about{left:111px;top:724px;width:977px;height:514px;background:var(--white);box-shadow:0 4px 30px rgba(0,0,0,.08)}
.about-img{left:154px;top:767px;width:429px;height:428px;background:linear-gradient(135deg,#3a3530,#2f6ab5 55%,#7acb3a 80%,#3b332c)}
.h-section{font-weight:800;font-size:38px;text-transform:uppercase;color:var(--ink)}
.h-section em{font-style:normal;font-weight:500;color:var(--orange)}
.about-text{left:652px;top:855px;width:392px;font-size:15.5px;line-height:24.7px;color:var(--text);text-align:justify}
.about-text p{margin-bottom:10px}
/* services */
.center{left:0;width:1200px;text-align:center}
.svc{position:absolute;top:1499px;width:305px;height:342px;border-left:1.5px solid #777;border-bottom:1.5px solid #777}
.svc.on{border-color:var(--orange)}
.svc .ph{position:absolute;left:8px;top:0;right:0;bottom:8px}
.svc .arr{position:absolute;right:0;bottom:8px;width:75px;height:75px;background:var(--white);display:flex;align-items:center;justify-content:center}
.svc.on .arr{background:var(--orange)}
.svc-t{position:absolute;top:1870px;font-size:17.5px;font-weight:600;text-transform:uppercase}
.svc-d{position:absolute;top:1904px;width:278px;font-size:15.5px;line-height:24.7px;color:var(--text);text-align:justify}
/* band */
.band-l{left:0;top:2068px;width:600px;height:429px;background:var(--orange)}
.band-r{left:600px;top:2068px;width:600px;height:429px;background:var(--dark)}
.band h3{font-size:42px;font-weight:800;color:var(--white);text-transform:uppercase}
.band-l p{position:absolute;left:111px;top:133px;width:416px;font-size:15.5px;line-height:24.7px;color:var(--white);text-align:justify;font-weight:500}
.band-r ul{position:absolute;left:72px;top:133px;list-style:none;color:var(--white);font-size:16px;line-height:24.7px;font-weight:500}
.band-r li{padding-left:30px;position:relative}
.band-r li:before{content:"";position:absolute;left:0;top:9px;width:7px;height:7px;border:1.5px solid var(--orange);border-radius:50%}
.seal{left:555px;top:2236px;width:90px;height:90px;border-radius:50%;background:var(--white);border:3px solid #ccc;z-index:2}
/* testimonials */
.tcard{position:absolute;top:2757px;width:305px;height:403px;background:var(--white);border-top:4px solid var(--orange);border-radius:10px;box-shadow:0 6px 28px rgba(0,0,0,.08);text-align:center;padding:70px 22px 0}
.avatar{position:absolute;left:107px;top:-47px;width:92px;height:92px;border-radius:50%;border:4px solid var(--orange);background:linear-gradient(#d9d3cc,#8e877f)}
.tcard h4{font-size:16px;font-weight:600;text-transform:uppercase}
.stars{color:var(--orange);font-size:12px;letter-spacing:3px;margin:2px 0 12px}
.tcard p{font-size:15.5px;line-height:26px;color:var(--text)}
.tarrow{position:absolute;top:2949px;width:36px;height:36px;border-radius:50%;display:flex;align-items:center;justify-content:center}
/* footer */
.footer{left:0;top:3268px;width:1200px;height:311px;background:var(--dark);color:var(--white)}
.footer h5{position:absolute;top:62px;font-size:17px;font-weight:700;text-transform:uppercase}
.foot-logo{position:absolute;left:111px;top:86px;width:168px;height:168px;border-radius:50%;background:var(--white);display:flex;align-items:center;justify-content:center}
.links{position:absolute;left:318px;top:108px;list-style:none;font-size:14.5px;line-height:36px}
.links li{padding-left:33px;position:relative}
.links li:before{content:"";position:absolute;left:2px;top:12px;width:12px;height:12px;border:3px solid var(--orange);border-radius:50%}
.fsmall{position:absolute;font-size:12.5px;line-height:21px}
.fsmall b{font-weight:500;text-transform:uppercase;font-size:13.5px}
.copy{left:0;top:3579px;width:1200px;height:52px;background:var(--orange);color:var(--white);font-size:13px;display:flex;align-items:center;justify-content:center}
</style>
</head>
<body>

<!-- header -->
<div class="abs logo-frame"><span>KESTREL</span></div>
<div class="abs topphone">
<svg width="28" height="28" viewBox="0 0 24 24"><path fill="#f47320" d="M6.6 10.8a15 15 0 0 0 6.6 6.6l2.2-2.2c.3-.3.7-.4 1-.2 1.1.4 2.3.6 3.6.6.6 0 1 .4 1 1V20c0 .6-.4 1-1 1A17 17 0 0 1 3 4c0-.6.4-1 1-1h3.5c.6 0 1 .4 1 1 0 1.3.2 2.5.6 3.6.1.3 0 .7-.2 1z"/></svg>
0400 555 817</div>
<div class="btn btn-orange" style="left:887px;top:16px;width:202px;height:48px">Get in touch today!</div>
<div class="abs nav"><span class="active">Home</span><span>About Us</span><span>Our Services</span><span>Completed Projects</span><span>Contact Us</span></div>
<div class="soc" style="left:1008px;top:85px"></div>
<div class="soc" style="left:1050px;top:85px"></div>

<!-- hero -->
<div class="abs hero" role="img" aria-label="Cleaner in protective suit and respirator working in a dusty roof space">
<h1 style="top:173px">KESTREL</h1>
<h2 style="top:243px">SERVICES PTY LTD</h2>
<p style="top:295px">Adelaide-based Kestrel Services is a family-run organisation. We have been in operation for more than two decades.</p>
</div>
<div class="btn btn-orange" style="left:111px;top:569px;width:197px;height:47px">Dirty Job Cleaners</div>
<div class="btn btn-white" style="left:316px;top:569px;width:196px;height:47px">Get a quote</div>
<div class="abs callbox">
<svg width="44" height="44" viewBox="0 0 24 24"><path fill="#fff" d="M6.6 10.8a15 15 0 0 0 6.6 6.6l2.2-2.2c.3-.3.7-.4 1-.2 1.1.4 2.3.6 3.6.6.6 0 1 .4 1 1V20c0 .6-.4 1-1 1A17 17 0 0 1 3 4c0-.6.4-1 1-1h3.5c.6 0 1 .4 1 1 0 1.3.2 2.5.6 3.6.1.3 0 .7-.2 1z"/></svg>
<div><small>CALL US TODAY:</small><b>0400 555 817</b></div>
</div>

<!-- about -->
<div class="abs about-accent"></div>
<div class="abs about"></div>
<div class="abs about-img" role="img" aria-label="Worker in blue protective suit holding a green tub of debris in a fire-damaged room"></div>
<div class="abs h-section" style="left:652px;top:790px">About <em>Us</em></div>
<div class="abs about-text">
<p>Adelaide-based Kestrel Services is a family-run organisation. We have been in operation for more than two decades. We've gained some knowledge about cleaning and squalor removal services throughout the years.</p>
<p>As a small South Australian company, we base everything on responsibility honesty and fairness .We are aware of the confidence you put in us when you seek our help.</p>
</div>
<div class="btn btn-orange" style="left:653px;top:1114px;width:142px;height:48px">Learn more</div>

<!-- services -->
<div class="abs h-section center" style="top:1346px;font-size:40px">Our <em>Services</em></div>
<div class="abs center" style="top:1413px;font-size:17.5px;line-height:28px;color:var(--text)">We are fully insured for 20 million public liability and our team have current police and working<br>with vunerable people clearances</div>

<div class="svc" style="left:111px"><div class="ph" role="img" aria-label="Worker clearing pigeon droppings from a roof gutter" style="background:linear-gradient(160deg,#8a7250,#3d3b34 50%,#1f1f1f)"></div><div class="arr"><svg width="48" height="24" viewBox="0 0 48 24"><path d="M2 12h42M34 3l10 9-10 9" stroke="#f47320" stroke-width="3" fill="none"/></svg></div></div>
<div class="svc on" style="left:447px"><div class="ph" role="img" aria-label="Fire-damaged kitchen with burnt stove and exposed insulation" style="background:linear-gradient(170deg,#5a4b48,#2b2725 55%,#1a1716)"></div><div class="arr"><svg width="48" height="24" viewBox="0 0 48 24"><path d="M2 12h42M34 3l10 9-10 9" stroke="#fff" stroke-width="3" fill="none"/></svg></div></div>
<div class="svc" style="left:783px"><div class="ph" role="img" aria-label="Cluttered shed with shelves of stored items" style="background:linear-gradient(160deg,#6e6150,#8d7d66 45%,#4a4036)"></div><div class="arr"><svg width="48" height="24" viewBox="0 0 48 24"><path d="M2 12h42M34 3l10 9-10 9" stroke="#f47320" stroke-width="3" fill="none"/></svg></div></div>

<div class="svc-t" style="left:111px">Pigeon Waste</div>
<div class="svc-t" style="left:447px;text-decoration:underline">Fire Damage Clean Outs</div>
<div class="svc-t" style="left:783px">Squlaor Estate Clean Ups</div>
<div class="svc-d" style="left:111px">Can cause damage to buildings and spread disease, mites and bacteria, triggering alarms</div>
<div class="svc-d" style="left:447px">Removal of debris; On site cleaning of contents; Cleaning of carpets and upholstered items</div>
<div class="svc-d" style="left:783px">Kestrel Services is a hoarding clean up firm that approaches clutter removal personally.</div>

<!-- pricing / qualifications -->
<div class="abs band band-l"><h3 style="position:absolute;left:111px;top:62px">Pricing</h3>
<p>Prices provided in terms of the number of hours and service required or as a fixed quotation according to the quantity of clutter, pigeon faeces, and mould disposal expenses; however, hoarding cleaning can be different as this may require sorting and can require more organisation.</p></div>
<div class="abs band band-r"><h3 style="position:absolute;left:72px;top:62px">Qualifications</h3>
<ul><li>Mould Remediation CRSB Standard S520</li><li>CRSB Standard Trauma &amp; Crime Scene Cleans</li><li>White Card</li><li>Working at Heights</li><li>National Police Cleared</li><li>Working with vunerable people (DHS)</li></ul></div>
<div class="abs seal"></div>
<div class="btn btn-white" style="left:111px;top:2377px;width:197px;height:48px">Get a quote</div>
<div class="btn btn-orange" style="left:673px;top:2377px;width:197px;height:48px">Get a quote</div>

<!-- testimonials -->
<div class="abs center" style="top:2600px;font-size:40px;font-weight:800;text-transform:uppercase;line-height:48px">Only the best service</div>
<div class="abs center" style="top:2650px;font-size:38px;font-weight:500;color:var(--orange);text-transform:uppercase;line-height:48px">For our customers</div>

<div class="tcard" style="left:111px"><div class="avatar" role="img" aria-label="Customer portrait"></div><h4>Helena Morvane</h4><div class="stars">★★★★★</div><p>Daniel and his team arrived the next morning to clean up a rental property my husband and I own which and had been trashed by the tenants. He was the only contractor to return my call. They did an amazing job and also deodorised the house for no extra charge.</p></div>
<div class="tcard" style="left:447px"><div class="avatar" role="img" aria-label="Customer portrait"></div><h4>Tessa Lindqvist</h4><div class="stars">★★★★★</div><p>Excellent service. Very happy with outcome Did the job as quoted.</p></div>
<div class="tcard" style="left:783px"><div class="avatar" role="img" aria-label="Customer portrait"></div><h4>Owen Pratley</h4><div class="stars">★★★★★</div><p>Engaged Kestrel Services to clean bird poo from our commercial building facade . Job was so well done it exceeded our expectations.</p></div>
<div class="tarrow" style="left:43px;background:#fde6d6"><svg width="12" height="14" viewBox="0 0 12 14"><path d="M9 1 3 7l6 6" stroke="#f47320" stroke-width="2" fill="none"/></svg></div>
<div class="tarrow" style="left:1121px;background:var(--orange)"><svg width="12" height="14" viewBox="0 0 12 14"><path d="M3 1l6 6-6 6" stroke="#fff" stroke-width="2" fill="none"/></svg></div>

<!-- footer -->
<div class="abs footer">
<div class="foot-logo"><span>KESTREL</span></div>
<h5 style="left:318px">Quick Links</h5>
<ul class="links"><li>Home</li><li>About Us</li><li>Our Services</li><li>Completed Projects</li><li>Contact Us</li></ul>
<h5 style="left:545px">Get a Quick Quote</h5>
<div class="fsmall" style="left:541px;top:110px;width:290px">Got more questions about our clean-up services and what we offer?<br>Get in touch today M <span style="color:var(--orange)">0400 555 817</span></div>
<svg class="abs" style="left:541px;top:189px" width="13" height="13" viewBox="0 0 14 14"><circle cx="7" cy="7" r="5.5" stroke="#f47320" stroke-width="2" fill="none"/><path d="M7 4v3h2" stroke="#f47320" stroke-width="1.5" fill="none"/></svg>
<div class="fsmall" style="left:570px;top:186px"><b>Business Hours:</b><br>Monday to Saturday, 8:00 am to 4:00 pm</div>
<h5 style="left:864px">Contact Info</h5>
<svg class="abs" style="left:864px;top:112px" width="11" height="14" viewBox="0 0 12 16"><path d="M6 0a6 6 0 0 1 6 6c0 4-6 10-6 10S0 10 0 6a6 6 0 0 1 6-6z" fill="#f47320"/><circle cx="6" cy="6" r="2" fill="#24282b"/></svg>
<div class="fsmall" style="left:902px;top:108px;font-size:11.5px;line-height:20px"><b>Address:</b><br>14 Larkin Avenue Norwood<br>SA 5067</div>
<svg class="abs" style="left:864px;top:190px" width="13" height="13" viewBox="0 0 24 24"><path fill="#f47320" d="M6.6 10.8a15 15 0 0 0 6.6 6.6l2.2-2.2c.3-.3.7-.4 1-.2 1.1.4 2.3.6 3.6.6.6 0 1 .4 1 1V20c0 .6-.4 1-1 1A17 17 0 0 1 3 4c0-.6.4-1 1-1h3.5c.6 0 1 .4 1 1 0 1.3.2 2.5.6 3.6.1.3 0 .7-.2 1z"/></svg>
<div class="fsmall" style="left:902px;top:186px;font-size:11.5px;line-height:20px"><b>Call:</b><br>Daniel or Priya 0400 555 817</div>
<svg class="abs" style="left:864px;top:240px" width="14" height="11" viewBox="0 0 14 11"><rect width="14" height="11" fill="#f47320"/><path d="M0 0l7 6 7-6" stroke="#24282b" stroke-width="1.5" fill="none"/></svg>
<div class="fsmall" style="left:902px;top:236px;font-size:11.5px;line-height:20px"><b>Email:</b><br>admin@kestrelservices.com</div>
</div>
<div class="abs copy">© 2025&nbsp;<span style="color:var(--dark)">KESTREL</span>&nbsp;&nbsp;|&nbsp;&nbsp;All Rights Reserved</div>
<div class="abs" style="left:1009px;top:3587px;width:36px;height:36px;border-radius:50%;background:var(--white)"></div>
<div class="abs" style="left:1051px;top:3587px;width:36px;height:36px;border-radius:50%;background:var(--white)"></div>
</body>
</html>
```